Poster Required for Cafe to promote coffee/staff discounts

Need an A3 size poster designed for our business to promote that we roast our own coffee, and that we offer discounts for staff.
I have attached a poster which we use to promote catering that our business offers, also have attached logos and our business card..
Also, I have attached our business card I would like the poster to look a little like that.
Eg. Our logo.
Then Specialty Coffee Roasters (under or next to this, in small print: Producing Slow Roasted Coffee)
Location
Download our App
Website
I would like the poster to state:
Tallowmere Health Staff receive $1 off their coffee or hot drink when presenting their staff pass.
Please don't hesitate to ask if you need more info.

```html
<!DOCTYPE html>
<html lang="en">
<head>
<meta charset="utf-8">
<title>Bedside Brew – Specialty Coffee Roasters</title>
<link rel="stylesheet" href="https://fonts.googleapis.com/css2?family=Arvo:wght@400;700&family=Questrial&family=PT+Sans+Narrow&family=Nunito+Sans:wght@800&display=swap">
<style>
  :root {
    --cream: #fbf5a7;
    --cream-light: #fcf7bd;
    --haze: #fbf9e6;
    --ink: #231f20;
    --paper: #ffffff;
    --bean-dark: #1c120c;
    --bean-mid: #5a3520;
    --bean-light: #8a5a38;
  }
  * { margin: 0; padding: 0; box-sizing: border-box; }
  html, body { width: 849px; height: 1200px; overflow: hidden; background: var(--cream); }
  .poster {
    position: relative;
    width: 849px;
    height: 1200px;
    overflow: hidden;
    color: var(--ink);
    background: linear-gradient(180deg, var(--cream) 0%, var(--cream) 58%, var(--cream-light) 66%, var(--haze) 70%, var(--cream-light) 74%, #e6e1b0 77%, #6d6a55 79%, var(--bean-dark) 80%);
  }
  .brand-badge {
    position: absolute;
    top: 66px;
    left: 278px;
    width: 292px;
    height: 292px;
    border-radius: 50%;
    background: var(--ink);
    display: flex;
    align-items: center;
    justify-content: center;
    text-align: center;
    font-family: "Questrial", sans-serif;
    font-size: 38px;
    line-height: 44px;
    letter-spacing: 4px;
    color: var(--paper);
    padding-bottom: 12px;
  }
  .headline {
    position: absolute;
    top: 414px;
    left: 0;
    width: 849px;
    text-align: center;
    font-family: "Arvo", serif;
    font-weight: 400;
    font-size: 52px;
    line-height: 50px;
    letter-spacing: 2px;
  }
  .tagline {
    position: absolute;
    top: 574px;
    left: 0;
    width: 849px;
    text-align: center;
    font-family: "Arvo", serif;
    font-size: 16px;
  }
  .divider {
    position: absolute;
    left: 164px;
    width: 518px;
    height: 2px;
    display: block;
  }
  .divider--top { top: 608px; }
  .divider--bottom { top: 823px; }
  .location {
    position: absolute;
    top: 636px;
    left: 0;
    width: 849px;
    text-align: center;
    font-family: "Questrial", sans-serif;
    font-size: 27px;
    letter-spacing: 0.5px;
  }
  .region {
    position: absolute;
    top: 674px;
    left: 0;
    width: 849px;
    text-align: center;
    font-family: "PT Sans Narrow", sans-serif;
    font-size: 25px;
    letter-spacing: 1px;
  }
  .app-button {
    position: absolute;
    top: 734px;
    left: 289px;
    width: 270px;
    height: 50px;
    border: 2px solid var(--ink);
    display: flex;
    align-items: center;
    justify-content: center;
    font-family: "PT Sans Narrow", sans-serif;
    font-size: 25px;
    letter-spacing: 1.5px;
  }
  .staff-offer {
    position: absolute;
    top: 794px;
    left: 0;
    width: 849px;
    text-align: center;
    font-family: "PT Sans Narrow", sans-serif;
    font-size: 17px;
    line-height: 20px;
    letter-spacing: 0.5px;
  }
  .website {
    position: absolute;
    top: 858px;
    left: 0;
    width: 849px;
    text-align: center;
    font-family: "Nunito Sans", sans-serif;
    font-weight: 800;
    font-size: 25px;
    letter-spacing: 0.5px;
  }
  .beans {
    position: absolute;
    top: 950px;
    left: 0;
    width: 849px;
    height: 250px;
    background:
      radial-gradient(ellipse 300px 120px at 30% 60%, var(--bean-light) 0%, rgba(138,90,56,0) 100%),
      radial-gradient(ellipse 300px 120px at 75% 70%, var(--bean-light) 0%, rgba(138,90,56,0) 100%),
      linear-gradient(180deg, var(--bean-dark) 0%, var(--bean-mid) 30%, var(--bean-mid) 100%);
  }
</style>
</head>
<body>
  <main class="poster">
    <div class="brand-badge">BEDSIDE<br>BREW</div>

    <h1 class="headline">SPECIALTY<br>COFFEE<br>ROASTERS</h1>
    <p class="tagline">Producing Slow Roasted Coffee</p>

    <svg class="divider divider--top" viewBox="0 0 518 2" aria-hidden="true">
      <line x1="0" y1="1" x2="518" y2="1" stroke="#231f20" stroke-width="2" stroke-dasharray="8 5"/>
    </svg>

    <p class="location">Located at Marrowvale Hospital</p>
    <p class="region">QUEENSLAND, AUSTRALIA</p>

    <div class="app-button">DOWNLOAD OUR APP</div>

    <p class="staff-offer">Tallowmere Health Staff receive $1 off their coffee or hot drink.</p>

    <svg class="divider divider--bottom" viewBox="0 0 518 2" aria-hidden="true">
      <line x1="0" y1="1" x2="518" y2="1" stroke="#231f20" stroke-width="2" stroke-dasharray="8 5"/>
    </svg>

    <p class="website">bedsidebrew.com.au</p>

    <div class="beans" role="img" aria-label="Photograph of roasted coffee beans spread across the bottom of the poster"></div>
  </main>
</body>
</html>
```